High Profile Wordpress Design for Marketing Agency

http://www.LanternCo.example.nz is moving from GridPortal to wordpress

Lantern Co is a leading New Zealand consumer brands public relations and advertising agency.
Our marketing agency represents some of the worlds most recognisable brands as well as some small independent businesses and everything in between.
Our GPL current site has served us well for 6+ years but we are now wanting to move to wordpress.

We are looking for a new look for our website which will be either a 2013 facelift keeping existing colour scheme rather than a radical new design
Our target market is marketing managers and brand owners familiar with design and marketing elements.
First and foremost the site must be functional from an SEO and loading speed point of view. To assist this we want to retain the text content.
Secondly we have historically had only pointers to other pages on our site but we want to incorporate more of the highlights of our services and our portfolio with the addition of some 'sample boxes' such as in this template: http://vendorplace.example/item/sample-business-theme/full_screen_preview/5821307

Wordpress offers an easier interface for uploading news items which we do daily and also take advantage of the plugins for seo. We are looking to redesign the look of the site while keeping all the existing text content.

Logo – also needs refreshing. Something corporate but not staid. Modern and clean.

Existing pages
- We want a fresh new clean look while retaining the orange and gray colours. white space is good. modern fonts are good.
- Social media : we want to focus on Google Plus primarily but also facebook and twitter. We suggest a funky design with the social media logos. Social media logos on all pages.
- Add New page: client coverage. A page to showcase new client coverage. Could be print, links to online video, mepgs, etc. Perhaps as a blog?
- Add New page: Advertising (as a service).

Home page. Perhaps a larger image existing image can be used or something new that says Stand out from the crowd (but not in a clichéd way). perhaps 3-4 main images could be used which rotate? We want to use stunning image(s) on the site.
Retain existing body of text somewhere on page.

an alternative idea might be to look at images which relate to news. and use the phrase "journalists reaching journalists"

Add Small ‘boxes’ on home page – teasers for content inside the site:
- Our clients logo box. Perhaps use a mouse over to ‘roll’ logos from homepage? Plus link to our clients page. http://www.lanternco.example.nz/OurClients/CurrentClients.aspx
- Our services
- Quotes about us. Show an image of Harbourline magazine with quote about us
- Advertising box: Featured project (as embedded youtube clip and link case study)
- Contact us page – refresh look simple details only.

Client News (blog) page:

Image(s) to top right rather than bottom.
Google Plus like one and share as first icon. Also facebook, twitter share and RSS. (moving icons which scroll down as reader moves down?)

Hi Budget on this project to redesign Auckland PR Firm Lantern Co's website in wordpress has been increased significantly to A$2190

Target Market(s)

Marketing managers, small - large business owners
we are primarily a public relations firm, then advertising. focus should be on these services rather than web design/seo etc which are a secondary part of our offering.

Industry/Entity Type

Advertising

Requirements
Must have
• must retain existing text content(for seo reasons)
fast loading, free of slow graphics
mobile/tablet friendly
new logo
Google Plus 1 logo
Should not have
• our agency is slightly on the conservative side and yet we are looking for a modern look.
prefer light over dark colour scheme/images
Images – better to not use people in images. people from stock images tend to give the impression of an international site and we are looking closer to NZ

```html
<!DOCTYPE html>
<html lang="en">
<head>
<meta charset="utf-8">
<title>Lantern Co – Public Relations &amp; Advertising, Auckland</title>
<link rel="stylesheet" href="https://fonts.googleapis.com/css2?family=Open+Sans:wght@300;400&family=Noto+Serif:ital@0;1&family=Arimo:wght@400;700&display=swap">
<style>
:root{
  --orange:#fbaa26;
  --ink:#222;
  --text:#444;
  --nav:#555;
  --muted:#7a7a7a;
  --hero-dark:#3a3a3a;
  --hero-darker:#2e2e2e;
  --panel:#f7f7f7;
  --line:#e2e2e2;
  --white:#fff;
}
*{box-sizing:border-box;margin:0;padding:0}
html,body{width:1200px;height:990px;overflow:hidden;background:var(--white)}
body{position:relative;font-family:"Arimo",Arial,sans-serif;color:var(--ink)}

.topbar{position:absolute;left:0;top:0;width:1200px;height:33px;background:var(--orange);color:var(--white);font-size:11.5px;font-weight:700}
.topbar .contact{position:absolute;left:158px;top:10px;display:flex;gap:20px;align-items:center}
.topbar .contact span{display:flex;align-items:center;gap:7px}
.topbar .social{position:absolute;left:853px;top:7px;display:flex;gap:11px}
.topbar .social i{display:block;width:15px;height:15px;border-radius:50%;background:var(--white)}

.masthead{position:absolute;left:0;top:33px;width:1200px;height:125px}
.brand{position:absolute;left:220px;top:43px;font-family:"Open Sans",sans-serif;font-weight:300;font-size:37px;line-height:44px;color:var(--text)}
.nav{position:absolute;left:418px;top:55px;height:20px;display:flex;align-items:center;border-left:2px solid var(--orange);padding-left:11px;font-family:"Noto Serif",serif;font-size:13.5px}
.nav a{color:var(--nav);text-decoration:none;margin-right:20px;display:flex;align-items:center;gap:6px}
.nav a:last-child{margin-right:0}
.nav .caret{width:0;height:0;border-left:3px solid transparent;border-right:3px solid transparent;border-top:4px solid #777}

.hero{position:absolute;left:0;top:158px;width:1200px;height:425px;overflow:hidden}
.hero-art{position:absolute;inset:0 0 7px 0;background:
  radial-gradient(ellipse 260px 150px at 340px 418px,rgba(251,170,38,.85),rgba(251,170,38,0) 100%),
  linear-gradient(135deg,var(--hero-dark),var(--hero-darker) 60%,#363636)}
.hero .cta{position:absolute;left:278px;top:362px;display:flex;align-items:center;gap:22px;font-family:"Open Sans",sans-serif;font-size:36px;line-height:44px;color:var(--white)}
.shot{position:absolute;background:linear-gradient(180deg,#fff 0 12%,#444 12% 57%,#fff 57%);box-shadow:0 0 8px rgba(0,0,0,.35)}
.shot.main{left:663px;top:72px;width:325px;height:346px}
.shot.tablet{left:563px;top:152px;width:100px;height:266px}
.shot.phone{left:988px;top:216px;width:73px;height:202px}
.hero-rule{position:absolute;left:0;bottom:0;width:1200px;height:7px;background:var(--orange)}

.callout{position:absolute;left:158px;top:638px;width:846px;height:100px;border:1px solid var(--line);border-left:2px solid var(--orange);border-right:2px solid var(--orange);background:var(--panel);text-align:center}
.callout h1{font-family:"Open Sans",sans-serif;font-weight:400;font-size:24px;line-height:30px;color:var(--ink);margin-top:27px}
.callout p{font-size:12px;line-height:16px;color:var(--muted);margin-top:5px}

.services{position:absolute;left:158px;top:800px;width:846px}
.service{position:absolute;top:0;width:280px}
.service:nth-child(1){left:0}
.service:nth-child(2){left:287px}
.service:nth-child(3){left:575px}
.service .badge{position:absolute;left:0;top:2px;width:38px;height:38px;border-radius:50%;background:var(--orange)}
.service .badge svg{position:absolute;left:11px;top:11px}
.service h2{margin-left:53px;font-family:"Open Sans",sans-serif;font-weight:400;font-size:25px;line-height:30px;color:var(--ink)}
.service p{margin-left:53px;margin-top:10px;width:222px;font-size:12.5px;line-height:19px;color:var(--muted)}
.service a{display:block;margin-left:53px;margin-top:16px;font-family:"Noto Serif",serif;font-style:italic;font-size:12.5px;color:var(--orange);text-decoration:none}
</style>
</head>
<body>

<header class="topbar">
  <div class="contact">
    <span><svg width="10" height="13" viewBox="0 0 10 13"><rect x="1" y="0.7" width="8" height="11.6" rx="1" fill="none" stroke="#fff" stroke-width="1.4"/><rect x="3" y="2.5" width="4" height="4" fill="#fff"/></svg>0800-555-0142</span>
    <span><svg width="14" height="10" viewBox="0 0 14 10"><rect x="0.7" y="0.7" width="12.6" height="8.6" fill="none" stroke="#fff" stroke-width="1.4"/><path d="M1 1 7 6 13 1" fill="none" stroke="#fff" stroke-width="1.4"/></svg>hello@lanternco.example.nz</span>
    <span><svg width="8" height="13" viewBox="0 0 8 13"><path d="M5 0 0 7h3l-1 6 6-8H5z" fill="#fff"/></svg>Journalists reaching journalists</span>
  </div>
  <div class="social" aria-label="Social links"><i></i><i></i><i></i><i></i><i></i><i></i></div>
</header>

<div class="masthead">
  <div class="brand">Lantern Co</div>
  <nav class="nav">
    <a>Home <span class="caret"></span></a>
    <a>Services <span class="caret"></span></a>
    <a>Advertising <span class="caret"></span></a>
    <a>News <span class="caret"></span></a>
    <a>Coverage <span class="caret"></span></a>
    <a>Clients <span class="caret"></span></a>
    <a>Contact</a>
  </nav>
</div>

<section class="hero">
  <div class="hero-art" role="img" aria-label="Hero artwork: dark grey backdrop with soft circles and an orange cloud rising at the lower left"></div>
  <div class="cta">
    <svg width="48" height="34" viewBox="0 0 48 34"><path d="M8 32a8 8 0 0 1-1-16 12 12 0 0 1 23-5 9 9 0 0 1 13 8 7.5 7.5 0 0 1-1 13z" fill="#fff"/><path d="M24 11v13m-6-5 6 6 6-6" fill="none" stroke="var(--orange)" stroke-width="3"/></svg>
    <span>Talk To Us</span>
  </div>
  <div class="shot tablet" role="img" aria-label="Tablet-width preview of the Lantern Co home page"></div>
  <div class="shot phone" role="img" aria-label="Phone-width preview of the Lantern Co home page"></div>
  <div class="shot main" role="img" aria-label="Desktop preview of the Lantern Co home page"></div>
  <div class="hero-rule"></div>
</section>

<section class="callout">
  <h1>Stand Out From The Crowd, Not In It</h1>
  <p>Lantern Co is a leading New Zealand consumer brands public relations and advertising agency.</p>
</section>

<section class="services">
  <article class="service">
    <div class="badge"><svg width="16" height="16" viewBox="0 0 16 16"><circle cx="10" cy="6" r="3.5" fill="#fff"/><path d="M8 8 3 13" stroke="#fff" stroke-width="2.5"/></svg></div>
    <h2>Public Relations</h2>
    <p>We represent some of the world's most recognisable brands as well as small independent businesses, putting their stories in front of the journalists who matter.</p>
    <a>Learn More</a>
  </article>
  <article class="service">
    <div class="badge"><svg width="16" height="16" viewBox="0 0 16 16"><path d="M10 2 4 9h3l-1 5 6-7H9z" fill="#fff"/></svg></div>
    <h2>Advertising</h2>
    <p>From print to online video, our advertising team builds campaigns that work hand in hand with your PR, with featured projects and case studies to show it.</p>
    <a>Learn More</a>
  </article>
  <article class="service">
    <div class="badge"><svg width="16" height="16" viewBox="0 0 16 16"><circle cx="8" cy="8" r="5" fill="#fff"/><circle cx="8" cy="8" r="2" fill="var(--orange)"/></svg></div>
    <h2>Client Coverage</h2>
    <p>See the latest coverage we have won for our clients, updated daily with print features, online stories and broadcast links from across New Zealand.</p>
    <a>Learn More</a>
  </article>
</section>

</body>
</html>
```